Wandering Past Chronicles - Book Cover Design

I need a cover (front, spine, back) designed for the second edition of the historical book - Wandering Past Chronicles. This book was created to be a more engaging supplementary resource to the dry texts of most middle and high school social studies classrooms. Although comprehensive and exhaustively researched, the book at times uses humor and irony to engage the reader. The cover should reflect this tone.

Book Title: Wandering Past Chronicles
Subtitle: The Legends, Customs and Crossroads of Human Memory and the Local Dilemmas of Our Age
Author: Tobias Holloway
Updates

Project Deadline Extended
Reason: As multiple designers are working on adjustments and I am looking for new, creative ideas, I am extending the deadline five days. Thank you.

Project Deadline Extended
Reason: Artists are still making alterations to suggestions made and I also want to give designers a chance to submit new ideas.

Target Market(s)

Middle School and High School Teachers

Font styles to use
Serif

Colors
ec1f27
ffffff
000000

Requirements
Must have
• 1) See attachment for text for front cover, spine, back cover
• 2) Central, engaging image
Nice to have
• A subtle hint of humor, light tone
• Potentially upside down globe spinning
• Prefer black, red, white color scheme
Should not have
• Cartoonish text, images

```html
<!DOCTYPE html>
<html lang="en">
<head>
<meta charset="utf-8">
<title>Wandering Past Chronicles – Cover</title>
<link href="https://fonts.googleapis.com/css2?family=Rozha+One&family=Libre+Baskerville:wght@400;700&family=PT+Sans:wght@400;700&display=swap" rel="stylesheet">
<style>
  :root {
    --red: #ec1f27;
    --red-dark: #8e1116;
    --ink: #000000;
    --paper: #fbfbf9;
    --stage: #e6e6e6;
    --text: #1a1a1a;
    --art-light: #5a5a5a;
    --art-dark: #1c1c1c;
  }
  * { box-sizing: border-box; margin: 0; padding: 0; }
  html, body { width: 1200px; height: 1200px; overflow: hidden; }
  body {
    background: var(--stage);
    display: flex; align-items: center; justify-content: center;
    font-family: "PT Sans", sans-serif;
    color: var(--text);
  }
  .cover-spread {
    display: flex; width: 1116px; height: 840px;
    box-shadow: 0 10px 30px rgba(0,0,0,.18);
  }

  /* Back cover */
  .back-cover {
    width: 540px; height: 100%; background: var(--paper);
    padding: 56px 44px 40px; position: relative;
  }
  .back-cover__heading { font-size: 24px; font-weight: 700; margin-bottom: 14px; }
  .back-cover__blurb {
    font-size: 14.2px; line-height: 1.42; text-align: justify; margin-bottom: 14px;
  }
  .back-cover__blurb em { font-weight: 700; font-style: italic; }
  .back-cover__rule { border: 0; border-top: 2px solid var(--ink); margin: 22px 0 14px; }
  .back-cover__quote { font-size: 14.2px; line-height: 1.42; }
  .back-cover__quote strong { font-weight: 700; }
  .back-cover__code-box {
    position: absolute; right: 44px; bottom: 48px;
    width: 200px; height: 120px; border: 1.5px solid var(--ink); background: #fff;
  }

  /* Spine */
  .spine {
    width: 36px; height: 100%; background: var(--red);
    display: flex; align-items: center; justify-content: space-between;
    flex-direction: column; padding: 26px 0 30px; color: #fff;
  }
  .spine__title, .spine__author {
    writing-mode: vertical-rl; font-family: "Libre Baskerville", serif;
  }
  .spine__title { font-size: 20px; letter-spacing: 1px; white-space: nowrap; }
  .spine__author { font-size: 10px; line-height: 1.2; text-align: center; }

  /* Front cover */
  .front-cover {
    width: 540px; height: 100%; background: var(--paper);
    display: flex; flex-direction: column; align-items: center;
    padding: 52px 30px 40px; text-align: center;
  }
  .front-cover__edition {
    font-family: "Libre Baskerville", serif; font-weight: 700; font-size: 26px;
  }
  .front-cover__art {
    width: 280px; height: 320px; margin: 26px 0 18px;
    border-radius: 6px;
    background: radial-gradient(circle at 45% 55%, var(--art-light), var(--art-dark) 75%);
  }
  .front-cover__title {
    font-family: "Rozha One", serif; color: var(--red);
    font-size: 62px; line-height: 1; text-transform: uppercase;
    text-shadow: 2px 2px 0 var(--red-dark);
  }
  .front-cover__subtitle {
    font-family: "Libre Baskerville", serif; font-size: 19px; line-height: 1.3;
    margin-top: 18px; color: var(--text);
  }
  .front-cover__author {
    font-family: "Libre Baskerville", serif; font-size: 40px; margin-top: 14px;
  }
</style>
</head>
<body>
  <main class="cover-spread">
    <section class="back-cover">
      <h2 class="back-cover__heading">Do you know how we got to here?</h2>
      <p class="back-cover__blurb">Well, if you're like 97.4% of the people walking the planet, you haven't got a clue. Sure, you might know a bit about a couple rivers in Mesopotamia, how Thessalon wandered around Athens asking questions or how Brother Anselm Kray got ticked off one day and nailed a really long essay to the door of a church. But to be honest (and don't be embarrassed), you've got some gaps. Be dense no more. In <em>Wandering Past Chronicles</em>, Tobias Holloway once again takes you through all the major tales, traditions and turning points of world history - not just European history, but WORLD history. You'll figure out real quick that the West might have had some crowning moments, but for the whole of human history, it's been the Persians, the Indians, the Chinese, the Muslims or some horse peoples from the steppe that have truly turned us into the clever little creatures we are today.</p>
      <p class="back-cover__blurb">And while most world history books fade off once the Cold War comes to a close, this sometimes sardonic tome just gets going. Updated to include contemporary debates over topics such as Brexit, the rise of ISIS, claims to the South China Sea, the mounting refugee crisis and the controversial presidency of Dalton Crane, this second edition finishes with a distinctively comprehensive look at the 21st century challenges facing nine major regions of today's world - Africa, Latin America, Japan, China, the Middle East, India, Russia, Europe and the United States.</p>
      <hr class="back-cover__rule">
      <p class="back-cover__quote">"Tobias Holloway expertly understands what his audience wants to know, what they need to know. A page-turning account of our proudest achievements and our most colossal bumblings. It's world history for the rest of us." - <strong>Idris al-Wazzan</strong></p>
      <div class="back-cover__code-box"></div>
    </section>

    <aside class="spine">
      <span class="spine__title">WANDERING PAST CHRONICLES</span>
      <span class="spine__author">Tobias Holloway<br>Second Edition</span>
    </aside>

    <section class="front-cover">
      <p class="front-cover__edition">Second Edition</p>
      <div class="front-cover__art" role="img" aria-label="Central black silhouette illustration: two horse riders atop a spinning globe"></div>
      <h1 class="front-cover__title">Wandering<br>Past<br>Chronicles</h1>
      <p class="front-cover__subtitle">The Legends, Customs and Crossroads<br>of Human Memory<br>and the Local Dilemmas of Our Age.</p>
      <p class="front-cover__author">Tobias Holloway</p>
    </section>
  </main>
</body>
</html>
```